Ledgerwise Business Card Design

Business Card Design for new business called Ledgerwise focused on selling business software to small and medium size companies who have outgrown Tallymark. Similar companies would be Tallymark, Nuvo, CoreFlow. Also Dealharbor would be good to look at for additional ideas around look and feel.

Target Market(s)

Business to Business

Industry/Entity Type

Information Technology

Contact Information for Business Card

Standard Business Card Information

Font styles to use
Sans Serif

```html
<!DOCTYPE html>
<html lang="en">
<head>
<meta charset="UTF-8">
<title>Ledgerwise Business Card</title>
<link rel="stylesheet" href="https://fonts.googleapis.com/css2?family=Montserrat:wght@700&family=Encode+Sans+Condensed:wght@600&family=Roboto:wght@400&family=Open+Sans:wght@400&display=swap">
<style>
  :root {
    --navy: #0f4a7f;
    --orange: #f0820f;
    --paper: #ffffff;
    --backdrop: #ebe9e6;
    --ink: #1b4b7c;
  }
  * { margin: 0; padding: 0; box-sizing: border-box; }
  html, body {
    width: 1193px; height: 1200px; overflow: hidden;
    background: var(--backdrop);
  }
  .card {
    position: absolute;
    width: 720px; height: 428px;
    background: var(--paper);
    overflow: hidden;
  }
  .card--front { left: 211px; top: 157px; }
  .card--back { left: 213px; top: 642px; }

  .brand {
    position: absolute;
    display: flex; align-items: center; gap: 18px;
    font-family: "Montserrat", sans-serif;
    font-weight: 700;
    color: var(--navy);
    letter-spacing: -1px;
    white-space: nowrap;
  }
  .brand__dot {
    border-radius: 50%;
    background: var(--orange);
    flex: none;
  }
  .card--front .brand { left: 124px; top: 170px; font-size: 66px; }
  .card--front .brand__dot { width: 86px; height: 86px; }
  .card--back .brand { left: 36px; top: 90px; font-size: 52px; }
  .card--back .brand__dot { width: 68px; height: 68px; }

  .card__wave { position: absolute; left: 0; top: 0; }

  .contact {
    position: absolute; left: 35px; top: 282px;
    font-family: "Roboto", sans-serif;
    font-size: 17.5px; color: var(--ink);
    list-style: none;
  }
  .contact__item { display: flex; align-items: center; height: 27px; }
  .contact__icon { width: 18px; height: 14px; margin-right: 16px; }
  .contact__address { margin-top: -1px; }

  .person {
    position: absolute; right: 137px; top: 280px;
    text-align: right;
  }
  .person__name {
    font-family: "Encode Sans Condensed", sans-serif;
    font-weight: 600; font-size: 27px;
    color: var(--navy);
  }
  .person__title {
    font-family: "Open Sans", sans-serif;
    font-size: 16.5px; color: var(--ink);
    margin-top: 4px;
  }
</style>
</head>
<body>
  <section class="card card--front">
    <div class="brand"><span class="brand__name">Ledgerwise</span><span class="brand__dot"></span></div>
  </section>

  <section class="card card--back">
    <svg class="card__wave" width="720" height="428" viewBox="0 0 720 428" aria-hidden="true">
      <path d="M425 0 L720 0 L720 428 L606 428 C668 330 660 150 425 0 Z" fill="var(--navy)"/>
      <path d="M398 0 C630 150 672 330 584 428" fill="none" stroke="var(--orange)" stroke-width="6"/>
      <path d="M588 178 C632 222 646 292 640 352" fill="none" stroke="var(--orange)" stroke-width="4"/>
    </svg>

    <div class="brand"><span class="brand__name">Ledgerwise</span><span class="brand__dot"></span></div>

    <ul class="contact">
      <li class="contact__item">
        <svg class="contact__icon" viewBox="0 0 18 14" aria-hidden="true"><path d="M1 5 C1 1 17 1 17 5 L14 6 L13 4 L5 4 L4 6 Z M4 7 L14 7 L16 13 L2 13 Z" fill="var(--orange)"/></svg>
        +00 111 222 3333
      </li>
      <li class="contact__item">
        <svg class="contact__icon" viewBox="0 0 18 14" aria-hidden="true"><rect x="1" y="1" width="16" height="12" fill="var(--orange)"/><path d="M1 1 L9 8 L17 1" fill="none" stroke="#fff" stroke-width="1.5"/></svg>
        yourname@yourwebsite.com
      </li>
      <li class="contact__item">
        <svg class="contact__icon" viewBox="0 0 18 14" aria-hidden="true"><circle cx="9" cy="7" r="6.5" fill="var(--orange)"/><path d="M2.5 7 H15.5 M9 0.5 V13.5 M9 0.5 C5 4 5 10 9 13.5 M9 0.5 C13 4 13 10 9 13.5" fill="none" stroke="#fff" stroke-width="1"/></svg>
        www.yourwebsite.com
      </li>
      <li class="contact__address">Your Long Commercial address 2 line</li>
    </ul>

    <div class="person">
      <p class="person__name">Your Long Name</p>
      <p class="person__title">Managing Director</p>
    </div>
  </section>
</body>
</html>
```